Luxury Bath Flyer

I would like to have a professional Flyer, which would describe a beautiful atmospheric luxury-Bath situation. I am sending you a( screenshot) Flyer Proposal, which shoes my intention and wish how I would like to have it. Please note that Ästhetik and a professional Flyer is very important to me. If possible send a psd.file or a indesign file, in case of we gonna need to change the text. You are also free to make 2 different proposals and one as you would suggest.?(I send you couple pictures, but the main one which I choose on the pdf file, please keep that, it is called " BE-03" - If there is a question please let me know. Looking forward to receive an amazing artwork.Kind Regards Dilek

```html
<!DOCTYPE html>
<html lang="de">
<head>
<meta charset="utf-8">
<title>Wohnwerk – Ihr exklusives Bad zum Fixpreis</title>
<link rel="stylesheet" href="https://fonts.googleapis.com/css2?family=Open+Sans:wght@400;600;700;800&family=Roboto:wght@300;400;500&family=Roboto+Condensed:wght@700&display=swap">
<style>
  :root {
    --dark: #2c2d2d;
    --orange: #ec6224;
    --blue: #1a6fc0;
    --white: #ffffff;
    --paper: #f4f4f5;
    --grey-bar: #7a7b7d;
    --black: #111213;
    --text-grey: #3a3a3a;
  }
  * { margin: 0; padding: 0; box-sizing: border-box; }
  html, body { width: 918px; height: 1200px; overflow: hidden; background: var(--paper); }
  .flyer { position: relative; width: 918px; height: 1200px; font-family: "Open Sans", sans-serif; }

  .hero-photo {
    position: absolute; left: 0; top: 0; width: 918px; height: 539px;
    background: linear-gradient(160deg, #5d534c 0%, #b7aea4 30%, #d9d3cb 55%, #8a7563 80%, #4c3d33 100%);
  }
  .hero-title {
    position: absolute; right: 54px; top: 42px; text-align: right;
    color: var(--white); font-weight: 700; font-size: 55px; line-height: 66px;
    text-shadow: 2px 3px 6px rgba(0,0,0,.55);
  }
  .hero-badge {
    position: absolute; left: 657px; top: 198px; width: 176px; height: 176px;
    border-radius: 50%; background: var(--white); border: 5px solid #e6e6e6;
    box-shadow: 0 4px 10px rgba(0,0,0,.35);
    display: flex; align-items: center; justify-content: center;
  }
  .brand-name { font-weight: 800; color: var(--black); font-size: 28px; }

  .web-tab { position: absolute; left: 50px; top: 505px; }
  .web-tab span {
    position: absolute; left: 0; top: 0; width: 390px; height: 46px;
    display: flex; align-items: center; justify-content: center;
    color: var(--white); font-weight: 700; font-size: 25px; letter-spacing: 1px;
  }

  .services-panel { position: absolute; left: 0; top: 539px; width: 918px; height: 378px; background: var(--dark); }
  .claim { position: absolute; left: 45px; top: 40px; color: var(--white); font-weight: 700; font-size: 45px; line-height: 57px; }
  .services { position: absolute; left: 47px; top: 188px; color: var(--white); }
  .services h2 { font-family: "Roboto", sans-serif; font-weight: 300; font-size: 31px; margin-bottom: 20px; }
  .services li, .benefits li { list-style: none; display: flex; align-items: center; }
  .services li { font-family: "Roboto", sans-serif; font-weight: 300; font-size: 18px; height: 27px; }
  .services li::before, .benefits li::before {
    content: ""; width: 13px; height: 13px; border-radius: 50%; margin-right: 7px; flex: none;
  }
  .services li::before { background: var(--orange); }

  .benefits {
    position: absolute; left: 516px; top: 188px; width: 350px; height: 161px;
    background: var(--orange); color: var(--white); padding: 10px 0 0 26px;
    box-shadow: 0 5px 8px rgba(0,0,0,.4);
  }
  .benefits h2 { font-family: "Roboto", sans-serif; font-weight: 300; font-size: 33px; margin-bottom: 10px; }
  .benefits li { font-family: "Roboto", sans-serif; font-weight: 500; font-size: 20px; height: 31px; }
  .benefits li::before { background: var(--white); border: 1px solid #555; }

  .gallery { position: absolute; top: 950px; height: 159px; box-shadow: 0 6px 8px rgba(0,0,0,.3); }
  .gallery--wash { left: 30px; width: 185px; background: linear-gradient(135deg, #8c6a62, #d8cfc8 60%, #6e625d); }
  .gallery--sink { left: 220px; width: 185px; background: linear-gradient(160deg, #6b6b6b, #c9b6a1 45%, #efeae4 70%, #9c7c5e); }
  .gallery--showroom { left: 409px; width: 210px; background: linear-gradient(180deg, #4a4e55, #bfbcb6 45%, #d8d4cf 70%, #3b3a3a); }

  .contact-block { position: absolute; left: 650px; top: 975px; width: 230px; text-align: center; color: var(--text-grey); }
  .contact-block .brand-name { display: block; font-size: 30px; margin-bottom: 44px; }
  .contact-block address { font-style: normal; font-size: 18px; line-height: 26px; }

  .footer-bar { position: absolute; left: 0; top: 1153px; width: 918px; height: 47px; background: var(--grey-bar); }
  .footer-email { position: absolute; left: 44px; top: 1163px; color: var(--white); font-size: 15px; letter-spacing: .5px; }
  .footer-call {
    position: absolute; left: 329px; top: 1132px; width: 537px; height: 68px; background: var(--black);
    color: var(--white); display: flex; align-items: center; padding-left: 20px; font-weight: 600; font-size: 20px;
  }
  .footer-call svg { position: absolute; left: -24px; top: 0; }
  .footer-call strong { font-family: "Roboto Condensed", sans-serif; font-size: 27px; margin-left: 6px; }
</style>
</head>
<body>
<div class="flyer">
  <div class="hero-photo" role="img" aria-label="Modernes Badezimmer mit Holzwaschtisch, Mosaikfliesen und freistehender Badewanne"></div>
  <h1 class="hero-title">Ihr exklusives<br>Bad zum Fixpreis!</h1>
  <div class="hero-badge"><span class="brand-name">Wohnwerk</span></div>

  <div class="web-tab">
    <svg width="390" height="46" viewBox="0 0 390 46">
      <path d="M0 46 Q10 46 20 30 L30 8 Q34 0 44 0 L320 0 Q330 0 334 8 L350 36 Q356 46 390 46 Z" fill="var(--blue)"/>
    </svg>
    <span>www.wohnwerk-bad.at</span>
  </div>

  <section class="services-panel">
    <p class="claim">Wir montieren für Sie...<br>und das „Alles aus einer Hand“!</p>
    <div class="services">
      <h2>UNSERE SERVICES</h2>
      <ul>
        <li>Markenbäder zum Online Preis</li>
        <li>Wir montieren für Sie</li>
        <li>Funktionalität und Ästhetik</li>
        <li>Komplettlösungen mit rasche Umsetzung</li>
      </ul>
    </div>
    <div class="benefits">
      <h2>Ihre Vorteile</h2>
      <ul>
        <li>Individuelle Badplanung</li>
        <li>Eigene Handwerker vor Ort</li>
        <li>Traumbad erlebniss</li>
      </ul>
    </div>
  </section>

  <div class="gallery gallery--wash" role="img" aria-label="Aufsatzwaschbecken vor rosafarbener Wand mit rundem Spiegel"></div>
  <div class="gallery gallery--sink" role="img" aria-label="Weißes Waschbecken mit Armatur vor Mosaikfliesen"></div>
  <div class="gallery gallery--showroom" role="img" aria-label="Badausstellung mit Handtuchheizkörper und Badmöbeln"></div>

  <div class="contact-block">
    <span class="brand-name">Wohnwerk</span>
    <address>Birkenallee 12,<br>2351 Wiesenfeld</address>
  </div>

  <div class="footer-bar"></div>
  <p class="footer-email">Email: office@wohnwerk-bad.at</p>
  <div class="footer-call">
    <svg width="24" height="68" viewBox="0 0 24 68"><path d="M24 0 L24 68 L0 68 L0 21 Z" fill="var(--black)"/></svg>
    Feel Free to Contact us Today; <strong>0800 314 962</strong>
  </div>
</div>
</body>
</html>
```